Velvet Orchard Website A Website design for book editing

A website design for book editing

Our proofreading, editing and manuscript review packages are specifically tailored to help you publish the best possible version of your story.

NEED HELP PUBLISHING A BESTSELLER?

If you’re looking for professional book editing services from senior publishing industry insiders, look no further. Besides editing, we can also answer all your publishing questions and get you started building your author platform.

OUR SERVICES

We've carefully structured our packages to maximize value for every budget.

PRICING

$.02
PER WORD
Proofreading
Line Edit (Copy-editing)
Fix spelling and grammar
Sales copy/summary revision

$.04
PER WORD
Proofreading
Line Edit (Copy-editing)
Fix spelling and grammar
Organization and content
Plot and pacing
Manuscript Review

$.06
PER WORD
Proofreading
Line Edit (Copy-editing)
Fix spelling and grammar
Organization and content
Plot and pacing
Manuscript Review
Formatting (print and ebook)
Pre-publication proofread

OUR PROCESS

Send us a sample of your book. Our caffeine-fueled, eagle-eyed editors will go through it and then email you with their comments and suggestions. You can ask them any questions you want. They will look for…

Typos and grammatical errors.
Spelling and word choice issues
Punctuation and style
Word choice, clarity and flow.
Sentence structure and craft
If your writing is already clean, then they’ll discuss bigger picture things with you, like theme, concept, purpose, audience, potential market and branding (including title, subtitle, and tagline or elevator pitch).

Once you feel comfortable and confident in an editor’s expertise, skill and knowledge, and are ready to move ahead, we’ll send an invoice for the first half of the total word count so the editor can get started. We’ll charge the rest when the project is close to completion.

Target Market(s)

Authors

Industry/Entity Type

Book Publisher

Coding

Coded - Design and coding required

Number of Pages Required

1 page

Requirements
Must have
• OUR SERVICES
• We've carefully structured our packages to maximize value for every budget.
• PRICING
• $.02
• PER WORD
• Proofreading
• Line Edit (Copy-editing)
• Fix spelling and grammar
• Sales copy/summary revision
• $.04
• PER WORD
• Proofreading
• Organization and content
• Plot and pacing
• Manuscript Review
• $.06
• PER WORD
• Proofreading
• Plot and pacing
• Manuscript Review
• Formatting (print and ebook)
• Pre-publication proofread

```html
<!DOCTYPE html>
<html lang="en">
<head>
<meta charset="utf-8">
<title>Velvet Orchard – Book Editing</title>
<link href="https://fonts.googleapis.com/css2?family=Questrial&family=Open+Sans:wght@400;600&display=swap" rel="stylesheet">
<style>
:root{
  --red:#e2001f;
  --ink:#222222;
  --muted:#555555;
  --grey-band:#efefef;
  --panel:#eeeeee;
  --rule:#cfcfcf;
  --white:#ffffff;
  --footer:#2b2b2b;
  --footer-text:#9a9a9a;
}
*{margin:0;padding:0;box-sizing:border-box}
html,body{width:1200px;height:3103px;overflow:hidden}
body{background:var(--white);color:var(--ink);font-family:"Open Sans",Arial,sans-serif;position:relative}
.display{font-family:"Questrial","Century Gothic",sans-serif}
.wrap{position:absolute;left:132px;width:936px}

/* header */
.site-header{position:absolute;top:0;left:0;width:1200px;height:108px;background:var(--white)}
.brand{position:absolute;left:132px;top:44px;display:flex;align-items:center;gap:10px;font-family:"Questrial",sans-serif;font-size:31px;color:var(--red)}
.brand-dot{width:14px;height:14px;border-radius:50%;background:var(--red)}
.header-mail{position:absolute;right:132px;top:20px;font-size:14px;color:var(--muted);display:flex;align-items:center;gap:8px}
.main-nav{position:absolute;right:132px;top:66px;display:flex;gap:37px;font-family:"Questrial",sans-serif;font-size:14px;color:var(--muted)}
.main-nav .active{color:var(--red)}

/* hero */
.hero{position:absolute;top:108px;left:0;width:1200px;height:507px;background:linear-gradient(100deg,#efe4dc 0%,#e6d2c6 40%,#c8a08f 70%,#a9806f 100%)}
.hero h1{position:absolute;left:132px;top:208px;font-family:"Questrial",sans-serif;font-weight:400;font-size:41px;line-height:50px;color:#2d2d2d;letter-spacing:.5px}
.hero-arrow{position:absolute;top:240px;width:28px;height:28px;border-radius:50%;background:rgba(80,80,80,.75);display:flex;align-items:center;justify-content:center}
.hero-arrow.prev{left:48px}.hero-arrow.next{right:48px}

/* intro */
.intro{top:683px;text-align:center;font-family:"Questrial",sans-serif;font-size:27px;line-height:38px;color:#222}
.intro-rule{position:absolute;top:834px;left:132px;width:936px;height:2px;background:var(--rule)}

.section-title{position:absolute;left:0;width:1200px;text-align:center;font-family:"Questrial",sans-serif;font-size:35px;color:var(--red);font-weight:400}

/* services */
.services{top:956px;display:flex;gap:21px}
.service-card{width:298px;height:232px;background:var(--red);color:var(--white);text-align:center;padding:36px 30px 0}
.service-card h3{font-family:"Questrial",sans-serif;font-weight:400;font-size:25px;margin:12px 0 10px}
.service-card p{font-size:11px;line-height:17px}

/* pricing */
.pricing-band{position:absolute;top:1266px;left:0;width:1200px;height:650px;background:var(--grey-band)}
.pricing{top:1401px;display:flex;gap:21px}
.price-card{width:298px;height:432px;background:var(--white);position:relative}
.price-head{height:103px;border-bottom:1px solid #e2e2e2;display:flex;align-items:baseline;padding:22px 0 0 26px}
.price-head .amount{font-family:"Questrial",sans-serif;font-size:52px;color:var(--red);font-weight:600;letter-spacing:-1px}
.price-head .unit{font-family:"Questrial",sans-serif;font-size:19px;margin-left:12px;color:#222}
.price-list{list-style:none;padding:22px 0 0 26px}
.price-list li{font-size:12px;line-height:27.5px;color:#333;position:relative;padding-left:10px}
.price-list li::before{content:"";position:absolute;left:0;top:12px;width:3px;height:3px;border-radius:50%;background:#666}
.btn{position:absolute;left:25px;top:378px;width:102px;height:36px;background:var(--red);color:var(--white);font-size:12px;display:flex;align-items:center;justify-content:center}

/* process */
.process{top:2046px;display:flex;gap:21px}
.step{width:298px;height:168px;border:2px solid var(--red);padding:18px 20px;color:var(--red)}
.step p{font-family:"Questrial",sans-serif;font-size:16px;line-height:20px;margin-top:12px}

.look-for{top:2261px;height:435px;display:flex}
.look-copy{width:468px;background:var(--panel);padding:36px 28px}
.look-copy h4{font-family:"Questrial",sans-serif;font-weight:400;font-size:21px;margin-bottom:14px}
.checks{list-style:none;margin-bottom:16px}
.checks li{font-family:"Questrial",sans-serif;font-size:15px;line-height:32px;display:flex;align-items:center;gap:12px}
.look-copy p{font-size:10.5px;line-height:17px;color:#444;margin-bottom:14px}
.look-photo{width:468px;height:435px;background:linear-gradient(135deg,#5e4a3a 0%,#3a2c24 45%,#1f1a19 75%,#6a5a48 100%)}

/* contact */
.contact-band{position:absolute;top:2779px;left:0;width:1200px;height:209px;background:var(--grey-band)}
.contact-row{top:2905px;display:flex;justify-content:space-between;font-size:16px;color:#333}
.contact-row span{display:flex;align-items:center;gap:8px}

/* footer */
.site-footer{position:absolute;top:2988px;left:0;width:1200px;height:115px;background:var(--footer)}
.footer-links{position:absolute;left:132px;top:38px;font-size:10px;color:var(--footer-text)}
.footer-links span{margin:0 6px}
.footer-copy{position:absolute;left:132px;top:60px;font-size:10px;color:var(--footer-text)}
.social{position:absolute;right:136px;top:45px;display:flex;gap:8px}
.social i{width:25px;height:25px;border-radius:50%;background:#2f6db5;display:block}
.social i + i{background:#2aa0e0}
</style>
</head>
<body>

<header class="site-header">
  <div class="brand"><span class="brand-dot"></span>Velvet Orchard</div>
  <div class="header-mail">
    <svg width="14" height="11" viewBox="0 0 14 11"><rect x="0" y="0" width="14" height="11" rx="1" fill="#555"/><path d="M0 1 L7 6 L14 1" stroke="#fff" stroke-width="1.3" fill="none"/></svg>
    info@velvetorchard.com
  </div>
  <nav class="main-nav">
    <span class="active">Home</span><span>About Us</span><span>Services</span><span>Pricing</span><span>Our Process</span><span>Contact Us</span>
  </nav>
</header>

<section class="hero" role="img" aria-label="Photo of a hand writing with a black pen beside a cup, soft warm background">
  <h1>NEED HELP PUBLISHING<br>A BESTSELLER?</h1>
  <span class="hero-arrow prev"><svg width="10" height="12" viewBox="0 0 10 12"><path d="M7 1 L2 6 L7 11" stroke="#fff" stroke-width="2.2" fill="none"/></svg></span>
  <span class="hero-arrow next"><svg width="10" height="12" viewBox="0 0 10 12"><path d="M3 1 L8 6 L3 11" stroke="#fff" stroke-width="2.2" fill="none"/></svg></span>
</section>

<p class="wrap intro">Our proofreading, editing and manuscript review packages are specifically<br>tailored to help you publish the best possible version of your story.</p>
<div class="intro-rule"></div>

<h2 class="section-title" style="top:898px">OUR SERVICES</h2>
<div class="wrap services">
  <article class="service-card">
    <svg width="64" height="54" viewBox="0 0 64 54" fill="none" stroke="#fff" stroke-width="2.4"><path d="M4 4 H40 V28 H18 L10 36 V28 H4 Z"/><path d="M46 14 H60 V38 H54 V46 L46 38 H24 V32"/><path d="M11 13 H33 M11 20 H28"/></svg>
    <h3>Book Reviewing</h3>
    <p>Honest reader notes on voice, structure and pacing, delivered with clear advice for your next revision draft.</p>
  </article>
  <article class="service-card">
    <svg width="58" height="54" viewBox="0 0 58 54" fill="none" stroke="#fff" stroke-width="2.4"><path d="M6 6 H22 Q29 6 29 13 V50 Q29 44 22 44 H6 Z"/><path d="M52 6 H36 Q29 6 29 13 V50 Q29 44 36 44 H52 Z"/><path d="M2 12 V48 H56 V12"/><path d="M11 16 H23 M11 23 H23 M11 30 H23 M35 16 H47 M35 23 H47 M35 30 H47"/></svg>
    <h3>Book Publishing</h3>
    <p>From final files to release day, we guide layout, cover briefs and listings so your book is ready.</p>
  </article>
  <article class="service-card">
    <svg width="56" height="56" viewBox="0 0 56 56" fill="none" stroke="#fff" stroke-width="2.4"><path d="M30 6 H4 V52 H50 V26"/><path d="M46 4 L52 10 L28 34 L20 36 L22 28 Z"/></svg>
    <h3>Book Editing</h3>
    <p>Careful line and copy edits that sharpen every sentence while keeping your own voice intact on the page.</p>
  </article>
</div>

<div class="pricing-band"></div>
<h2 class="section-title" style="top:1343px">PRICING</h2>
<div class="wrap pricing">
  <article class="price-card">
    <div class="price-head"><span class="amount">$.02</span><span class="unit">PER WORD</span></div>
    <ul class="price-list">
      <li>Proofreading</li><li>Line Edit (Copy-editing)</li><li>Fix spelling and grammar</li><li>Sales copy/summary revision</li>
    </ul>
    <span class="btn">Sign Up Now</span>
  </article>
  <article class="price-card">
    <div class="price-head"><span class="amount">$.04</span><span class="unit">PER WORD</span></div>
    <ul class="price-list">
      <li>Proofreading</li><li>Line Edit (Copy-editing)</li><li>Fix spelling and grammar</li><li>Sales copy/summary revision</li><li>Organization and content</li><li>Plot and pacing</li><li>Manuscript Review</li>
    </ul>
    <span class="btn">Sign Up Now</span>
  </article>
  <article class="price-card">
    <div class="price-head"><span class="amount">$.06</span><span class="unit">PER WORD</span></div>
    <ul class="price-list">
      <li>Proofreading</li><li>Line Edit (Copy-editing)</li><li>Fix spelling and grammar</li><li>Sales copy/summary revision</li><li>Organization and content</li><li>Plot and pacing</li><li>Manuscript Review</li><li>Formatting (print and ebook)</li><li>Pre-publication proofread</li>
    </ul>
    <span class="btn">Sign Up Now</span>
  </article>
</div>

<h2 class="section-title" style="top:1988px">OUR PROCESS</h2>
<div class="wrap process">
  <article class="step">
    <svg width="36" height="28" viewBox="0 0 36 28"><rect width="36" height="28" rx="3" fill="#e2001f"/><path d="M1 3 L18 15 L35 3" stroke="#fff" stroke-width="2.6" fill="none"/></svg>
    <p>Send us a sample of your book</p>
  </article>
  <article class="step">
    <svg width="30" height="30" viewBox="0 0 30 30" fill="none" stroke="#e2001f"><circle cx="12" cy="12" r="9" stroke-width="4"/><path d="M19 19 L28 28" stroke-width="5" stroke-linecap="round"/></svg>
    <p>Our caffeine-fueled, eagle-eyed editors will go through it and then email you with their comments and suggestions.</p>
  </article>
  <article class="step">
    <svg width="30" height="30" viewBox="0 0 30 30"><circle cx="15" cy="15" r="15" fill="#e2001f"/><path d="M10.5 11.5 Q10.5 7 15 7 Q19.5 7 19.5 11 Q19.5 13.5 16.5 15 Q15 16 15 18" stroke="#fff" stroke-width="3" fill="none" stroke-linecap="round"/><circle cx="15" cy="22.5" r="2" fill="#fff"/></svg>
    <p>You can ask them any questions you want</p>
  </article>
</div>

<div class="wrap look-for">
  <div class="look-copy">
    <h4>They will look for…</h4>
    <ul class="checks">
      <li><svg width="15" height="12" viewBox="0 0 15 12"><path d="M1.5 6 L5.5 10 L13.5 2" stroke="#222" stroke-width="2.6" fill="none"/></svg>Typos and grammatical errors.</li>
      <li><svg width="15" height="12" viewBox="0 0 15 12"><path d="M1.5 6 L5.5 10 L13.5 2" stroke="#222" stroke-width="2.6" fill="none"/></svg>Spelling and word choice issues</li>
      <li><svg width="15" height="12" viewBox="0 0 15 12"><path d="M1.5 6 L5.5 10 L13.5 2" stroke="#222" stroke-width="2.6" fill="none"/></svg>Punctuation and style</li>
      <li><svg width="15" height="12" viewBox="0 0 15 12"><path d="M1.5 6 L5.5 10 L13.5 2" stroke="#222" stroke-width="2.6" fill="none"/></svg>Word choice, clarity and flow.</li>
      <li><svg width="15" height="12" viewBox="0 0 15 12"><path d="M1.5 6 L5.5 10 L13.5 2" stroke="#222" stroke-width="2.6" fill="none"/></svg>Sentence structure and craft</li>
    </ul>
    <p>If your writing is already clean, then they’ll discuss bigger picture things with you, like theme, concept, purpose, audience, potential market and branding (including title, subtitle, and tagline or elevator pitch).</p>
    <p>Once you feel comfortable and confident in an editor’s expertise, skill and knowledge, and are ready to move ahead, we’ll send an invoice for the first half of the total word count so the editor can get started. We’ll charge the rest when the project is close to completion.</p>
  </div>
  <div class="look-photo" role="img" aria-label="Photo of a reader holding an open book in a library with shelves of books"></div>
</div>

<div class="contact-band"></div>
<h2 class="section-title" style="top:2834px">Contact Info</h2>
<div class="wrap contact-row">
  <span><svg width="11" height="16" viewBox="0 0 11 16"><path d="M5.5 0 A5.5 5.5 0 0 1 11 5.5 C11 9 5.5 16 5.5 16 C5.5 16 0 9 0 5.5 A5.5 5.5 0 0 1 5.5 0 Z" fill="#333"/><circle cx="5.5" cy="5.5" r="2" fill="#efefef"/></svg>18 Linden Row, Harbor Street, Eastvale 40213</span>
  <span><svg width="14" height="14" viewBox="0 0 14 14"><path d="M3 0 L5.5 3.5 L4 5.5 Q5.5 8.5 8.5 10 L10.5 8.5 L14 11 L12 14 Q5 13 0 2 Z" fill="#333"/></svg>555 014 2297</span>
  <span><svg width="16" height="12" viewBox="0 0 16 12"><rect width="16" height="12" rx="1" fill="#333"/><path d="M0 1 L8 7 L16 1" stroke="#efefef" stroke-width="1.4" fill="none"/></svg>info@velvetorchard.com</span>
</div>

<footer class="site-footer">
  <div class="footer-links">Home<span>|</span>About Us<span>|</span>Services<span>|</span>Pricing<span>|</span>Our Process<span>|</span>Contact Us</div>
  <div class="footer-copy">Copyright © 2018 Velvet Orchard. All rights reserved.</div>
  <div class="social"><i></i><i></i></div>
</footer>

</body>
</html>
```